Commercial Cleaning Company specializing in windows and floors

Looking to have a brochure made for commercial cleaning company. Services include 2 categories:
1. Window Washing

2. Floor Cleaning and Restoration.

Within floor and cleaning restoration, there are several categories:
Carpet Cleaning & Restoration
-Tile and Grout Cleaning & Restoration
-Concrete Cleaning & Restoration
-Stone Cleaning & Restoration (Terrazzo, Marble, Limestone)
-VCT Cleaning & Restoration
-Wood Floor Cleaning & Restoration
-Epoxy Floor Cleaning & Restoration
Floor cleaning Text:
FLOOR CARE:

CARPET FLOORS
Low Moisture, Safe & Fast <--- Increase Font and color
Designed to support a healthy indoor environment, our carpet cleaning methods will eliminate the most common problems caused by other cleaning methods that lead to mold growth, mildew, volatile organic compounds (VOC), insufficient drying times, recurring stains and safety hazards. We also mitigate common safety hazards associated with multiple lengthy hoses, insecure open doors, and slippery hard surfaces. You'll find our system also eliminates both noise and emission pollution around your facility during cleaning times that are common with other cleaning methods.
Our low-moisture system supports a healthy indoor environment so carpets will stay clean & vibrant in color. With superior drying times, our methods eliminates mold growth and mildew. When we are finished cleaning, all that’s left are incredibly clean and fresh smelling carpets

TILE & GROUT FLOORS
We get deep into our cleaning <--- Increase Font and color
Tile and Grout floors can be very difficult to maintain. Often, dirt and grime get trapped in grout lines and crevices and discolor them, making the floors appear dirty. Our company has done all the experimenting for you, and we know the correct brushes, weight kits, machines, and chemical combinations to use to restore and maintain these types of floors, without leaving residue behind that will cause soil to return.

CONCRETE FLOORS
Pores & Crevices are no match <--- Increase Font and color
When it comes to scrubbing and cleaning concrete surfaces such as school hallways, patios, and other types of high traffic concrete flooring, we have you covered.
We're here to keep your employees and visitors safer. We eliminate having to use harsh chemicals and abundances of water to remove the heavy soil that has settled deep down in the concrete pores and crevices.

STONE FLOORS - TERRAZZO, MARBLE, LIMESTONE
We are experts in protecting your major flooring investment. <--- Increase Font and color
If you have high end stone floors, make sure they are performing their best for your facility. We can make educated recommendations on restoration schedules, cleaning methods, schedules, matting and everything related to making your floors "pop". These multi-step processes can be complex, but our experience ensures the best result for your building.

WOOD FLOORS
Wood floors can be tricky - We know how to clean and refinish them. <--- Increase Font and color
If you aren't careful, you may end up with undesirable results when dealing with wood floors. Traditional swing machines can leave swirls if not used correctly, and other methods may damage the wood. We've trained with leading wood floor companies to ensure a process that's safe for your floors and bring you the results you're looking for.

EPOXY FLOORS
We Clean Terrazzo, Flake coating, Screeds & More <--- Increase Font and color

Epoxy is protected from chemicals, dirt, liquids and other contaminants, however, Epoxy floors need to be cleaned routinely as they lose their original luster. We can restore any type of Epoxy floor and bring them back to life.

VCT/VINYL FLOORS <--- Increase Font and color

The most common floor types are our specialty
We can assist you in the maintenance of VCT and vinyl floors. We are helpful resources for assistance with stripping and re coating, daily maintenance, burnishing, and restorative buffing. We have worked with major pad manufacturers and chemical companies to help make selections on the best possible floor maintenance system for these common floors.

Window cleaning Text:
WINDOW CARE:
Our goal is to leave your employees and visitors with the best possible impression of your facility, and clean windows are a huge part of that. BrightHaven uses the latest pure water technology and equipment to leave your windows sparkling clean. We are trained to identify the correct process for various interior and exterior windows, as well as performing restorative processes for things like hard water deposits.
Older cleaning methods often leave behind streaking or residues. BrightHave has invested in equipment that utilizes de-ionized water, microfibers, and state of the art filtration. Recent designs in pole construction allow us to access hard to reach windows, facades, solar panels, sills, and ledges without the use of heavy equipment.
We offer a spate of maintenance programs the ensure the lowest total cost of cleaning. Inquire with us to learn more about why contracting these important cleaning tasks to Brighthaven will relieve you of: equipment storage and maintenance , brush selection, filtration concerns - as well as the liability of work that can sometimes present danger to untrained employees.

Company Biography Page:

BrightHaven is a family based company located in the greater Houston area that specializes in commercial floor care and window cleaning. Our mission is to prioritize the health and safety of the people who use your building by offering cleaning methods that are safe and use the latest industry technology. We understand that a clean, well maintained building has a direct relationship with your image - and that can have a direct effect on your bottom line or reputation. Please consider us for further consultation if you are interested in a no obligation discussion about your facility.

The management of BrightHaven has spent their entire professional lives in the commercial cleaning industry. We have recently sold facility supply distribution company and understand the facility maintenance industry top to bottom. In that time, we've met with innumerable manufacturers, distributors, trade groups, trainers and end users to gain insight into national and regional cleaning trends and methods. We understand budgets, compliance requirements, workflow timelines, and restorative schedules that you don't typically find in a contract cleaning company.
We are confident you will benefit from our wide range of experience and expertise when it comes to maintaining your facility.

Layout:

I think it would work best to have a 4 page single fold booklet type brochure - but open to any suggestions.
The inside would have the 2 services - one side hard floors and the other side windows. Either the front or the back would have our biography on it (probably the back?).
I will give you more input like the address and phone number at the end, it can be added easily.

For the pictures I've added:
The ones that include the word "example" are to be used when incorporating the services.

I've also included a bunch of window pictures. You can use some or none of these (and get other ones) in companion with the text about window cleaning.

Target Market(s)

Commercial buildings and institutions looking for our specific cleaning services

Industry/Entity Type

Commercial Cleaning

Font styles to use
Serif
Sans Serif

Colors
0054AA
0677BA
7BADD7
CADEEF
E8F1F8
0094D4
00A9DD
6FCCEA
C7EBF8
E9F6FB
59FF00
82FF00
B8FF75
E3FFCB
F4FFEA

Requirements
Must have
• All of the included text (can be edited slightly)
Nice to have
• Additional images or text gleened from other sources or past experience that help communicate our business

```html
<!DOCTYPE html>
<html lang="en">
<head>
<meta charset="utf-8">
<title>BrightHaven Brochure</title>
<link href="https://fonts.googleapis.com/css2?family=Archivo+Black&family=Poppins:wght@600;800&family=Roboto:wght@400;500;700&display=swap" rel="stylesheet">
<style>
:root{
  --green:#66cc22;
  --blue:#0054aa;
  --blue-mid:#0677ba;
  --cyan:#00a9dd;
  --ice:#cadeef;
  --ink:#222;
  --body:#3a3a3a;
  --paper:#ffffff;
  --bg:#f2f2f0;
}
*{margin:0;padding:0;box-sizing:border-box}
html,body{width:1200px;height:2625px;overflow:hidden}
body{position:relative;background:var(--bg);font-family:"Roboto",Arial,sans-serif;color:var(--body)}
.abs{position:absolute}
.photo{position:absolute}
.display{font-family:"Archivo Black",Impact,sans-serif}

/* spread one */
.quote-block{left:25px;top:786px;width:174px;height:124px;background:var(--green);color:#fff;font-family:"Archivo Black",sans-serif;font-size:110px;line-height:1;padding:12px 0 0 44px}
.brand-cell{left:25px;top:910px;width:174px;height:125px;background:var(--paper);display:flex;align-items:center;justify-content:center;gap:6px}
.brand{font-family:"Poppins",sans-serif;font-weight:800;color:var(--blue);display:flex;align-items:center;gap:8px}
.brand .dot{display:inline-block;border-radius:50%;background:var(--green)}
.about-panel{left:198px;top:786px;width:402px;height:733px;background:var(--blue);opacity:.97}
.about-title{left:234px;top:822px;color:#fff;font-size:28px}
.about-text{left:237px;top:884px;width:325px;color:#fff;font-size:14.4px;line-height:19.6px;text-align:justify}
.about-text p+p{margin-top:19px}
.contact-band{left:25px;top:1519px;width:1153px;height:157px;background:var(--green)}
.contact-block{left:738px;top:1580px;width:440px;height:96px;background:var(--blue)}
.contact-title{left:61px;top:1546px;color:#fff;font-size:24px}
.contact-rule{width:4px;height:41px;background:#fff}
.contact-line{color:#fff;font-size:16px;line-height:23px;font-weight:500}
.right-bar{left:666px;top:786px;width:512px;height:47px;background:var(--green)}
.right-strip{left:884px;top:991px;width:294px;height:43px;background:var(--blue)}
.cover-card{left:600px;top:1284px;width:536px;height:296px;background:#eef1ee;display:flex;align-items:center;justify-content:center}
.cover-edge{left:1136px;top:1284px;width:42px;height:296px;background:#3d7a2a;opacity:.7}

/* spread two */
.floor-page{left:25px;top:1694px;width:868px;height:891px;background:var(--paper)}
.floor-head{left:25px;top:1694px;width:576px;height:112px;background:linear-gradient(180deg,#1f5fb0,#0054aa)}
.floor-strip{left:336px;top:1784px;width:265px;height:35px;background:var(--green)}
.floor-title{left:70px;top:1756px;color:#fff;font-size:34px}
.floor-title-cut{left:25px;top:1796px;width:311px;height:23px;background:var(--paper)}
.svc{position:absolute;width:230px}
.svc h3{font-family:"Poppins",sans-serif;font-weight:800;font-size:13px;line-height:17px;color:var(--ink);text-transform:uppercase}
.svc .tag{font-family:"Poppins",sans-serif;font-weight:800;font-size:10px;line-height:16px;color:var(--cyan);text-transform:uppercase;margin-top:2px}
.svc .copy{font-size:9.2px;line-height:13.3px;text-align:justify;margin-top:12px}
.svc .copy p+p{margin-top:13px}
.floor-brand{left:336px;top:1843px;width:230px;height:97px;display:flex;align-items:center;justify-content:center}

.window-panel{left:892px;top:1694px;width:286px;height:891px;background:var(--green)}
.window-title{left:920px;top:1714px;color:#fff;font-size:38px;line-height:36px}
.window-copy{position:absolute;left:918px;width:236px;color:#fff;font-size:9.2px;line-height:13.3px;text-align:justify}
</style>
</head>
<body>

<!-- Spread one: about and cover -->
<div class="abs quote-block" aria-hidden="true">“</div>
<div class="abs brand-cell"><span class="brand" style="font-size:18px"><span class="dot" style="width:12px;height:12px"></span>BrightHaven</span></div>
<div class="photo" style="left:25px;top:1035px;width:174px;height:484px;background:linear-gradient(90deg,#8a8f94,#d8dadc 55%,#b9c0c6)" role="img" aria-label="Curved office facade with tall glass windows"></div>
<div class="abs about-panel"></div>
<h2 class="abs about-title display">About Us</h2>
<div class="abs about-text">
  <p>BrightHaven is a family based company located in the greater Houston and College Station areas that specializes in commercial floor care and window cleaning. Our mission is to prioritize the health and safety of the people who use your building by offering cleaning methods that are safe and use the latest industry technology. We understand that a clean, well maintained building has a direct relationship with your image - and that can have a direct effect on your bottom line or reputation. Please consider us for further consultation if you are interested in a no obligation discussion about your facility.</p>
  <p>The management of BrightHaven has spent their entire professional lives in the commercial cleaning industry. We have recently sold facility supply distribution company and understand the facility maintenance industry top to bottom. In that time, we've met with innumerable manufacturers, distributors, trade groups, trainers and end users to gain insight into national and regional cleaning trends and methods. We understand budgets, compliance requirements, workflow timelines, and restorative schedules that you don't typically find in a contract cleaning company.</p>
  <p>We are confident you will benefit from our wide range of experience and expertise when it comes to maintaining your facility.</p>
</div>

<div class="abs contact-band"></div>
<div class="abs contact-block"></div>
<h2 class="abs contact-title display">Contact Us</h2>
<div class="abs contact-rule" style="left:61px;top:1604px"></div>
<div class="abs contact-line" style="left:88px;top:1600px">+1234-567-890<br><b>www.website.com</b></div>
<div class="abs contact-rule" style="left:264px;top:1604px"></div>
<div class="abs contact-line" style="left:289px;top:1598px;font-weight:700">123 Anywhere St. Any City,<br>ST 12345</div>

<div class="abs right-bar"></div>
<div class="photo" style="left:600px;top:833px;width:284px;height:201px;background:linear-gradient(135deg,#2b6fc4,#9cc6ef 45%,#1c3f72)" role="img" aria-label="Glass office tower against a bright sky"></div>
<div class="photo" style="left:903px;top:833px;width:275px;height:158px;background:linear-gradient(90deg,#b9cfe0,#f3f3f1 50%,#c9d3da)" role="img" aria-label="Bright lobby with round columns and red seating"></div>
<div class="abs right-strip"></div>
<div class="photo" style="left:600px;top:1052px;width:578px;height:528px;background:linear-gradient(180deg,#c7dcb6,#8fb08a 60%,#4f7a4a)" role="img" aria-label="Open plan office with glass partitions and carpet, green tint"></div>
<div class="abs cover-card"><span class="brand" style="font-size:52px"><span class="dot" style="width:34px;height:34px"></span>BrightHaven</span></div>
<div class="abs cover-edge"></div>

<!-- Spread two: floor care and window care -->
<div class="abs floor-page"></div>
<div class="photo floor-head" role="img" aria-label="Row of chairs in a blue toned room"></div>
<div class="abs floor-strip"></div>
<div class="abs floor-title-cut"></div>
<h2 class="abs floor-title display">Floor Care</h2>

<!-- column one -->
<div class="photo" style="left:70px;top:1833px;width:230px;height:78px;background:linear-gradient(180deg,#5b5f66 40%,#b0162a 60%)" role="img" aria-label="Hall with red carpet"></div>
<section class="svc" style="left:70px;top:1934px">
  <h3>Carpeted Floors</h3>
  <div class="tag">Low Moisture, Safe &amp; Fast</div>
  <div class="copy">
    <p>Designed to support a healthy indoor environment, our carpet cleaning methods will eliminate the most common problems caused by other cleaning methods that lead to mold growth, mildew, volatile organic compounds (VOC), insufficient drying times, recurring stains and safety hazards. We also mitigate common safety hazards associated with multiple lengthy hoses, insecure open doors, and slippery hard surfaces. You'll find our system also eliminates both noise and emission pollution around your facility during cleaning times that are common with other cleaning methods.</p>
    <p>Our low-moisture system supports a healthy indoor environment so carpets will stay clean &amp; vibrant in color. With superior drying times, our methods eliminates mold growth and mildew. When we are finished cleaning, all that's left are incredibly clean and fresh smelling carpets.</p>
  </div>
</section>
<div class="photo" style="left:70px;top:2270px;width:230px;height:78px;background:linear-gradient(90deg,#e9e9e9,#c8202c 30%,#eeeeee 55%,#c8202c 75%,#e6e6e6)" role="img" aria-label="Tiled washroom with red cubicle doors"></div>
<section class="svc" style="left:70px;top:2373px">
  <h3>Tile &amp; Grout Floors</h3>
  <div class="tag">We get deep into our cleaning</div>
  <div class="copy">
    <p>Tile and Grout floors can be very difficult to maintain. Often, dirt and grime get trapped in grout lines and crevices and discolor them, making the floors appear dirty. Our company has done all the experimenting for you, and we know the correct brushes, weight kits, machines, and chemical combinations to use to restore and maintain these types of floors, without leaving residue behind that will cause soil to return.</p>
  </div>
</section>

<!-- column two -->
<div class="abs floor-brand"><span class="brand" style="font-size:26px"><span class="dot" style="width:18px;height:18px"></span>BrightHaven</span></div>
<div class="photo" style="left:336px;top:1970px;width:230px;height:78px;background:linear-gradient(180deg,#dfe6ec,#9fb59a 55%,#c5c2bb)" role="img" aria-label="Covered concrete walkway beside a garden"></div>
<section class="svc" style="left:336px;top:2075px">
  <h3>Concrete Floors</h3>
  <div class="tag">Pores &amp; Crevices are no match</div>
  <div class="copy">
    <p>When it comes to scrubbing and cleaning concrete surfaces such as hallways, patios, and other types of high traffic concrete flooring, we have you covered. We're here to keep your employees and visitors safer. We eliminate having to use harsh chemicals and abundances of water to remove the heavy soil that has settled deep down in the concrete pores and crevices.</p>
  </div>
</section>
<div class="photo" style="left:336px;top:2247px;width:230px;height:78px;background:linear-gradient(180deg,#3b3f46,#b21d2c 50%,#d9d9d9)" role="img" aria-label="Airport lounge with red seats on polished stone"></div>
<section class="svc" style="left:336px;top:2345px">
  <h3>Stone Floors - Terrazzo, Marble, Limestone</h3>
  <div class="tag">We are experts in protecting your major flooring investment</div>
  <div class="copy" style="margin-top:10px">
    <p>If you have high end stone floors, make sure they are performing their best for your facility. We can make educated recommendations on restoration schedules, cleaning methods, schedules, matting and everything related to making your floors "pop". These multi-step processes can be complex, but our experience ensures the best result for your building.</p>
  </div>
</section>

<!-- column three -->
<div class="photo" style="left:639px;top:1722px;width:232px;height:76px;background:linear-gradient(180deg,#ececec 55%,#a77a52)" role="img" aria-label="Empty room with red curtains and wood floor"></div>
<section class="svc" style="left:639px;top:1827px;width:232px">
  <h3>Wood Floors</h3>
  <div class="tag" style="line-height:15px">Wood floors can be tricky - We know how to clean and refinish them.</div>
  <div class="copy">
    <p>If you aren't careful, you may end up with undesirable results when dealing with wood floors. Traditional swing machines can leave swirls if not used correctly, and other methods may damage the wood. We've trained with leading wood floor companies to ensure a process that's safe for your floors and bring you the results you're looking for.</p>
  </div>
</section>
<div class="photo" style="left:639px;top:2018px;width:232px;height:78px;background:linear-gradient(180deg,#2d3036,#a5333b 55%,#c9c6c2)" role="img" aria-label="Cafeteria with red chairs on vinyl floor"></div>
<section class="svc" style="left:639px;top:2124px;width:232px">
  <h3>VCT/Vinyl Floors</h3>
  <div class="tag">The most common floor types are our specialty</div>
  <div class="copy">
    <p>We can assist you in the maintenance of VCT and vinyl floors. We are helpful resources for assistance with stripping and re coating, daily maintenance, burnishing, and restorative buffing. We have worked with major pad manufacturers and chemical companies to help make selections on the best possible floor maintenance system for these common floors.</p>
  </div>
</section>
<div class="photo" style="left:639px;top:2311px;width:232px;height:78px;background:linear-gradient(90deg,#b8cde0,#eeeeee 40%,#c1283a 70%,#dadada)" role="img" aria-label="Lobby with red sofas on glossy epoxy floor"></div>
<section class="svc" style="left:639px;top:2417px;width:232px">
  <h3>Epoxy Floors</h3>
  <div class="tag">We clean Terrazzo, Flake coating, Screeds &amp; More</div>
  <div class="copy">
    <p>Epoxy is protected from chemicals, dirt, liquids and other contaminants, however, Epoxy floors need to be cleaned routinely as they lose their original luster. We can restore any type of Epoxy floor and bring them back to life.</p>
  </div>
</section>

<!-- window care -->
<div class="abs window-panel"></div>
<h2 class="abs window-title display">Window<br>Care</h2>
<div class="photo" style="left:918px;top:1825px;width:236px;height:139px;background:linear-gradient(135deg,#e3eaef,#8fa7b5 50%,#3f6a54)" role="img" aria-label="Squeegee wiping a wet window pane"></div>
<p class="window-copy" style="top:1992px">Our goal is to leave your employees and visitors with the best possible impression of your facility, and clean windows are a huge part of that. BrightHaven uses the latest pure water technology and equipment to leave your windows sparkling clean. We are trained to identify the correct process for various interior and exterior windows, as well as performing restorative processes for things like hard water deposits.</p>
<div class="photo" style="left:918px;top:2141px;width:236px;height:158px;background:linear-gradient(135deg,#0b3f8c,#4d93d8 50%,#0e4a9a)" role="img" aria-label="Water spray and squeegee on glass in blue tones"></div>
<p class="window-copy" style="top:2327px">Older cleaning methods often leave behind streaking or residues. <b>BrightHave</b> has invested in equipment that utilizes de-ionized water, microfibers, and state of the art filtration. Recent designs in pole construction allow us to access hard to reach windows, facades, solar panels, sills, and ledges without the use of heavy equipment.</p>
<p class="window-copy" style="top:2436px">We offer a spate of maintenance programs the ensure the lowest total cost of cleaning. Inquire with us to learn more about why contracting these important cleaning tasks to <b>Brighthaven</b> will relieve you of: equipment storage and maintenance, brush selection, filtration concerns - as well as the liability of work that can sometimes present danger to untrained employees.</p>

</body>
</html>
```